Business Folder

I need a fresh, modern design for a business folder. I have our company's colors, logo, and a separate file for just the graphic part of our logo as a design element. No photo, just colors, gradients, and shadows to create depth. I like the idea of a rich grey as the background, however, I realize we'd have to lighten to 'Tax Advisory Services' part of our logo.

The design would just be the 'front' or outside of the folder from Mellowfax. Design file attached. You can find that here under 9 x 12 standard folder, Left and Right Pockets With Slit Both Sides:

https://www.mellowfax-example.com/content.html?id=folderDownloadTemplates&rightMenuId=rightMenu&footerId=bodyFooterStyle6

```html
<!DOCTYPE html>
<html lang="en">
<head>
<meta charset="utf-8">
<title>Mellowfax Business Folder – Inside Spread</title>
<link rel="stylesheet" href="https://fonts.googleapis.com/css2?family=Montserrat:wght@400;600&display=swap">
<style>
  :root {
    --stage: #1e1e1e;
    --paper: #f1f1f1;
    --pattern-light: #ececec;
    --pattern-mid: #dcdcdc;
    --pocket-deep: #0a4677;
    --pocket-mid: #1f5888;
    --pocket-glow: #4a7ea3;
    --slit: #e8eef4;
    --spine: #c9c9c9;
  }
  * { box-sizing: border-box; margin: 0; padding: 0; }
  html, body {
    width: 1200px; height: 833px; overflow: hidden;
    background: var(--stage);
    font-family: "Montserrat", sans-serif;
  }
  .folder-spread {
    position: absolute; left: 40px; top: 43px;
    width: 1120px; height: 747px;
    display: flex;
    box-shadow: 0 18px 40px rgba(0,0,0,.55);
  }
  .folder-panel {
    position: relative;
    width: 560px; height: 747px;
    background: var(--paper);
    overflow: hidden;
  }
  .folder-panel--left { border-right: 1px solid var(--spine); }
  .brand-pattern {
    position: absolute; inset: 0 0 auto 0; height: 480px;
    background:
      repeating-linear-gradient(135deg, rgba(0,0,0,.035) 0 18px, transparent 18px 44px),
      linear-gradient(180deg, var(--pattern-light), var(--pattern-mid));
  }
  .pocket {
    position: absolute; bottom: 14px; height: 270px;
    width: 532px;
  }
  .pocket--left {
    left: 14px;
    border-radius: 0 34px 0 0;
    background: linear-gradient(100deg, var(--pocket-deep) 0%, var(--pocket-mid) 55%, var(--pocket-glow) 90%);
  }
  .pocket--right {
    right: 14px;
    border-radius: 34px 0 0 0;
    background: linear-gradient(100deg, var(--pocket-deep) 0%, var(--pocket-glow) 35%, var(--pocket-mid) 70%, var(--pocket-deep) 100%);
  }
  .card-slits { position: absolute; inset: 0; width: 100%; height: 100%; }
  .card-slits line { stroke: var(--slit); stroke-width: 1.2; stroke-linecap: round; }
</style>
</head>
<body>
  <main class="folder-spread">
    <section class="folder-panel folder-panel--left">
      <div class="brand-pattern" role="img" aria-label="Repeating pattern of the Mellowfax brand symbol in light grey"></div>
      <div class="pocket pocket--left">
        <svg class="card-slits" viewBox="0 0 532 270" aria-hidden="true">
          <line x1="160" y1="58" x2="200" y2="44"/>
          <line x1="330" y1="150" x2="370" y2="136"/>
        </svg>
      </div>
    </section>
    <section class="folder-panel folder-panel--right">
      <div class="brand-pattern" role="img" aria-label="Repeating pattern of the Mellowfax brand symbol in light grey"></div>
      <div class="pocket pocket--right">
        <svg class="card-slits" viewBox="0 0 532 270" aria-hidden="true">
          <line x1="170" y1="70" x2="210" y2="56"/>
          <line x1="340" y1="200" x2="380" y2="186"/>
        </svg>
      </div>
    </section>
  </main>
</body>
</html>
```